Concrete Grinding and Polishing company business card with logo, based in Australia.

We need a business card design along with logo for a new company based in Melbourne called HexaSheen. We specialise in the grinding and polishing of concrete. Polished concrete is durable, easy to maintain, cost effective, dust proof, has increased light reflectivity, and is slip resistant, among other benefits. In short, polished concrete is a popular flooring solution because of its practical advantages, as well as it's decorative appeal.

Industry/Entity Type

Business

Requirements
Must have
• It must have the company name(HexaSheen) as well as the slogan: A Cut Above The Rest.
Nice to have
• Something that symbolises polished concrete. Would also like it to have a silver background with black writing, if possible.

```html
<!DOCTYPE html>
<html lang="en">
<head>
<meta charset="utf-8">
<title>HexaSheen – A Cut Above The Rest</title>
<link rel="stylesheet" href="https://fonts.googleapis.com/css2?family=Libre+Baskerville&family=Orbitron:wght@500&family=Questrial&display=swap">
<style>
  :root {
    --stage: #000000;
    --silver-dark: #8c8c8c;
    --silver-mid: #b9b9b9;
    --silver-light: #e2e2e2;
    --footer: #d9d9d9;
    --ink: #0a0a0a;
    --frame: #ffffff;
    --photo-top: #dfe6e8;
    --photo-bottom: #8e9a9d;
  }
  html, body {
    margin: 0;
    width: 880px;
    height: 1200px;
    overflow: hidden;
    background: var(--stage);
  }
  .card {
    position: absolute;
    left: 79px;
    top: 12px;
    width: 687px;
    height: 1132px;
    border-radius: 20px;
    overflow: hidden;
    background: var(--footer);
  }
  .card__face {
    position: absolute;
    left: 0; top: 0;
    width: 100%;
    height: 1007px;
    background: linear-gradient(180deg, var(--silver-dark) 0%, var(--silver-mid) 35%, var(--silver-light) 70%, var(--silver-light) 100%);
  }
  .card__sheen {
    position: absolute;
    left: 0; top: 0;
    width: 687px;
    height: 1007px;
  }
  .brand {
    position: absolute;
    left: 0;
    top: 28px;
    width: 100%;
    margin: 0;
    text-align: center;
    font-family: "Libre Baskerville", serif;
    font-weight: 400;
    font-size: 96px;
    line-height: 1;
    color: var(--ink);
    letter-spacing: -1px;
  }
  .slogan {
    position: absolute;
    left: 0;
    top: 170px;
    width: 100%;
    margin: 0;
    text-align: center;
    font-family: "Orbitron", sans-serif;
    font-weight: 500;
    font-size: 34px;
    letter-spacing: 3px;
    color: var(--ink);
    font-variant: small-caps;
  }
  .intro {
    position: absolute;
    left: 65px;
    top: 334px;
    width: 559px;
    margin: 0;
    font-family: "Libre Baskerville", serif;
    font-size: 18px;
    line-height: 27px;
    font-variant: small-caps;
    text-align: justify;
    text-align-last: center;
    color: var(--ink);
  }
  .photo {
    position: absolute;
    left: 183px;
    top: 599px;
    width: 341px;
    height: 275px;
    border: 3px solid var(--frame);
    background: linear-gradient(160deg, var(--photo-top) 0%, #b7c2c4 50%, var(--photo-bottom) 100%);
  }
  .band {
    position: absolute;
    left: 0;
    top: 1007px;
    width: 100%;
    height: 15px;
    background: var(--stage);
  }
  .contact {
    position: absolute;
    left: 0;
    top: 1040px;
    width: 100%;
    margin: 0;
    text-align: center;
    font-family: "Questrial", sans-serif;
    font-size: 21px;
    line-height: 26px;
    color: var(--ink);
    font-style: normal;
  }
</style>
</head>
<body>
  <main class="card">
    <div class="card__face">
      <svg class="card__sheen" viewBox="0 0 687 1007" aria-hidden="true">
        <path d="M0 0 H687 V30 C520 40 220 140 0 400 Z" fill="#ffffff" fill-opacity="0.16"/>
      </svg>
      <h1 class="brand">HexaSheen</h1>
      <p class="slogan">A Cut Above The Rest</p>
      <p class="intro">We specialise in the grinding and polishing of concrete. Polished concrete is durable, easy to maintain, cost effective, dust proof, has increased light reflectivity, and is slip resistant, among other benefits. In short, polished concrete is a popular flooring solution because of its practical advantages, as well as it's decorative appeal.</p>
      <div class="photo" role="img" aria-label="Photo of a hand resting on a stack of polished concrete blocks"></div>
    </div>
    <div class="band"></div>
    <address class="contact">
      E.mail : hello@hexasheen-floors.com<br>
      Phone : (03) 9421 7608
    </address>
  </main>
</body>
</html>
```